New Flyer Design Project

Needing brochure explaining the benefits of a home sleep study compared to a clinical hospital sleep study. We had our company logo designed by Lumen Forge, we love it. We would like for it to be a bi-fold. See attachments for examples of information we would like to include.

```html
<!DOCTYPE html>
<html lang="en">
<head>
<meta charset="utf-8">
<title>Prairie Rest CPAP – Home Sleep Study Bi-fold</title>
<link href="https://fonts.googleapis.com/css2?family=Poppins:ital,wght@0,400;0,500;0,600;0,700;1,600;1,700&family=Oswald:wght@400;500;600&display=swap" rel="stylesheet">
<style>
:root{
  --navy:#17428a;
  --blue:#1f56a6;
  --blue-deep:#133879;
  --green:#4cb648;
  --green-dark:#3a9a37;
  --ink:#2d3340;
  --muted:#4a5060;
  --paper:#ffffff;
  --stage:#5a5a5a;
  --photo-light:#e3e8f1;
  --photo-mid:#c5cfe0;
}
*{box-sizing:border-box;margin:0;padding:0}
html,body{width:1200px;height:3072px;overflow:hidden}
body{background:var(--stage);font-family:"Poppins",sans-serif;color:var(--ink);position:relative}
.spread{position:absolute;left:40px;width:1120px;height:792px;display:flex;box-shadow:0 6px 18px rgba(0,0,0,.35)}
.spread--outer{top:714px}
.spread--inner{top:1566px}
.page{position:relative;width:560px;height:792px;background:var(--paper);overflow:hidden}
.page > *{position:absolute}
.page-bg{left:0;top:0;width:560px;height:792px}
.photo{background:linear-gradient(160deg,var(--photo-light),var(--photo-mid))}
.photo-round{border-radius:50%;border:7px solid var(--green);background:radial-gradient(circle at 40% 35%,#f1ede8,#c9c6cc)}
.brand{display:flex;align-items:center;gap:10px;font-family:"Poppins",sans-serif;font-weight:600;white-space:nowrap}
.brand-mark{width:26px;height:26px}
.pill{border-radius:20px;color:#fff;font-weight:600;display:flex;align-items:center;justify-content:center;white-space:nowrap}
.pill--green{background:var(--green)}
.pill--navy{background:var(--navy)}
.web{font-size:14px;letter-spacing:.5px}
.dots{width:30px;height:16px;background:radial-gradient(circle,currentColor 2px,transparent 2.6px) 0 0/7.5px 8px}

/* back cover */
.back .brand{left:152px;top:318px;color:#fff;font-size:31px}
.back .brand-mark{background:#fff}
.back .title-pill{left:68px;top:385px;width:428px;height:38px;font-family:"Oswald",sans-serif;font-weight:500;font-size:28px;letter-spacing:.3px}
.back .lead{left:68px;top:436px;color:#fff;font-size:15px;font-weight:500;line-height:23px}
.back .facts{left:68px;top:493px;list-style:none;color:#fff;font-size:11px}
.back .facts li{position:relative;padding-left:18px;height:24px}
.back .facts li::before{content:"";position:absolute;left:0;top:3px;width:8px;height:8px;border-radius:50%;background:var(--green)}
.back .facts::before{content:"";position:absolute;left:3.5px;top:8px;width:1px;height:46px;background:var(--green)}
.back .order{left:68px;top:650px;color:var(--blue);font-size:12px;font-weight:700;line-height:14px}
.back .order strong{display:block;color:var(--green);font-size:29px;line-height:34px;letter-spacing:.5px}
.back .order-rule{left:68px;top:700px;width:180px;height:2px;background:var(--green)}
.back .phone{left:68px;top:708px;display:flex;align-items:center;gap:8px;color:var(--blue);font-size:23px;font-weight:700}
.back .web{left:336px;top:748px;color:var(--blue-deep)}
.back .dots{left:68px;top:752px;color:var(--blue)}

/* front cover */
.front .brand{left:118px;top:46px;color:var(--blue);font-size:34px}
.front .brand-mark{background:var(--green);width:28px;height:28px}
.front .headline{left:58px;top:206px;width:260px;font-family:"Oswald",sans-serif;font-weight:500;color:#fff;font-size:44px;line-height:48px;text-transform:uppercase;letter-spacing:-.5px;white-space:nowrap}
.front .headline .hl-green{color:var(--green)}
.front .headline .hl-big{font-size:62px;line-height:62px}
.front .rule{left:58px;top:432px;width:122px;height:3px;background:var(--green)}
.front .intro{left:58px;top:478px;width:216px;color:#fff;font-size:10.5px;line-height:14px}
.front .result-box{left:58px;top:568px;width:212px;height:82px;border:3px solid var(--green);padding:8px 14px;color:#fff;font-size:18.5px;line-height:22px}
.front .result-box span{color:var(--green)}
.front .web{left:328px;top:748px;color:var(--blue-deep)}
.front .dots{left:58px;top:752px;color:var(--blue)}

/* inner left */
.checklist-page .intro{left:58px;top:52px;width:400px;color:var(--blue);font-size:11.6px;font-weight:500;line-height:16px}
.checklist-page .check-pill{left:222px;top:118px;width:279px;height:27px;font-size:15px}
.checklist-page .ask{left:243px;top:186px;color:var(--blue);font-size:13px;font-weight:700;font-style:italic}
.steps{list-style:none;font-size:10.5px;line-height:14px;color:var(--ink)}
.steps li{position:relative;padding-left:18px}
.steps li::before{content:"";position:absolute;left:0;top:3px;width:8px;height:8px;border-radius:50%;border:1.5px solid var(--green);background:#fff}
.steps::before{content:"";position:absolute;left:4px;top:8px;bottom:8px;width:1px;background:var(--green)}
.checklist-page .quiz{left:226px;top:210px;width:240px}
.checklist-page .quiz li{margin-bottom:10px}
.checklist-page .verdict{left:222px;top:355px;width:280px;font-size:10.5px;font-weight:600;line-height:14px;color:var(--ink)}
.checklist-page .divider{left:91px;top:411px;width:425px;height:1px;background:#b9bfca}
.checklist-page .problem-pill{left:58px;top:423px;width:165px;height:25px;font-size:15px}
.checklist-page .subtitle{left:58px;top:458px;color:var(--blue);font-size:12.5px;font-weight:700;font-style:italic}
.checklist-page .problem-text{left:58px;top:475px;width:440px;font-size:10.5px;line-height:13px}
.checklist-page .list-head{left:58px;top:513px;font-size:10.5px;font-weight:700}
.checklist-page .lab-list{left:62px;top:532px;width:400px}
.checklist-page .lab-list li{margin-bottom:10px}
.checklist-page .dots{color:var(--blue)}
.checklist-page .dots--side{left:488px;top:585px;width:16px;height:30px;background-size:8px 7.5px}
.checklist-page .dots--foot{left:68px;top:752px;color:#fff}
.checklist-page .web{left:336px;top:750px;color:#fff}

/* inner right */
.compare-page .col-pill{top:229px;width:194px;height:27px;font-size:15px}
.compare-page .col-pill--home{left:59px}
.compare-page .col-pill--lab{left:306px}
.compare-page .col-rule{left:282px;top:270px;width:1px;height:222px;background:#c2c8d2}
.features{list-style:none;width:210px}
.features li{position:relative;padding-left:24px;height:53px;font-size:9.8px;line-height:12.5px;color:var(--ink)}
.features h3{font-size:12.5px;font-weight:600;line-height:16px}
.features svg{position:absolute;left:0;top:2px;width:15px;height:15px}
.features--home{left:66px;top:272px}
.features--home h3{color:var(--green)}
.features--lab{left:310px;top:272px}
.features--lab h3{color:var(--blue)}
.compare-page .divider{left:59px;top:504px;width:454px;height:1px;background:#c2c8d2}
.compare-page .results{left:59px;top:534px;font-size:15.5px;font-weight:700;line-height:19px;color:var(--blue)}
.compare-page .results span{color:var(--green)}
.compare-page .results-text{left:59px;top:584px;width:250px;font-size:10.5px;line-height:14px}
.compare-page .order-btn{left:59px;top:648px;width:166px;height:19px;font-size:10px;font-weight:500;border-radius:12px}
.compare-page .dots--foot{left:68px;top:752px;color:#fff}
.compare-page .web{left:336px;top:750px;color:#fff}
</style>
</head>
<body>

<!-- OUTER SPREAD -->
<section class="spread spread--outer">

  <article class="page back">
    <div class="photo" role="img" aria-label="Man sleeping in bed wearing a home sleep test device on his wrist" style="left:0;top:0;width:560px;height:400px"></div>
    <svg class="page-bg" viewBox="0 0 560 792" aria-hidden="true">
      <defs>
        <linearGradient id="backBlue" x1="0" y1="0" x2="0" y2="1">
          <stop offset="0" stop-color="#1f56a6" stop-opacity="0"/>
          <stop offset=".22" stop-color="#1f56a6" stop-opacity=".92"/>
          <stop offset="1" stop-color="#17428a"/>
        </linearGradient>
      </defs>
      <path d="M0 230 L560 250 L560 640 L0 640Z" fill="url(#backBlue)"/>
      <path d="M0 596 C170 628 360 650 560 548 L560 792 L0 792Z" fill="#fff"/>
      <path d="M0 582 C170 614 360 636 560 534 L560 552 C360 654 170 632 0 600Z" fill="#4cb648"/>
    </svg>
    <div class="brand"><span class="brand-mark"></span>Prairie Rest CPAP</div>
    <div class="pill pill--green title-pill">HOMEREST ONE HOME SLEEP TEST</div>
    <p class="lead">No appointments. No insurance chaos.<br>Just better sleep, made easy</p>
    <ul class="facts">
      <li>FDA Cleared Device, DOT Approved.</li>
      <li>Results in less than 72 Hours</li>
      <li>98 Percent Lab Accuracy</li>
    </ul>
    <div class="photo-round" role="img" aria-label="Woman resting peacefully on a pillow" style="left:304px;top:501px;width:206px;height:206px"></div>
    <p class="order">ORDER YOUR<strong>TEST KIT</strong></p>
    <div class="order-rule"></div>
    <div class="phone">
      <svg width="22" height="22" viewBox="0 0 24 24" aria-hidden="true"><path d="M6.6 10.8a15.2 15.2 0 0 0 6.6 6.6l2.2-2.2a1 1 0 0 1 1-.25 11.4 11.4 0 0 0 3.6.57 1 1 0 0 1 1 1V20a1 1 0 0 1-1 1A17 17 0 0 1 3 4a1 1 0 0 1 1-1h3.5a1 1 0 0 1 1 1c0 1.25.2 2.45.57 3.57a1 1 0 0 1-.25 1Z" fill="#1f56a6"/></svg>
      (555) 010 2468
    </div>
    <div class="dots"></div>
    <div class="web">www.prairierestcpap.com</div>
  </article>

  <article class="page front">
    <svg class="page-bg" viewBox="0 0 560 792" aria-hidden="true">
      <defs>
        <linearGradient id="frontBlue" x1="0" y1="0" x2="1" y2="1">
          <stop offset="0" stop-color="#1d4f9c"/>
          <stop offset="1" stop-color="#2a67b8"/>
        </linearGradient>
      </defs>
      <path d="M0 162 C200 160 420 146 560 88 L560 700 C380 760 180 720 0 738Z" fill="url(#frontBlue)"/>
      <path d="M0 146 C200 144 420 130 560 70 L560 94 C420 152 200 166 0 168Z" fill="#4cb648"/>
      <path d="M0 738 C180 720 380 762 560 698 L560 720 C380 784 180 744 0 760Z" fill="#4cb648"/>
    </svg>
    <div class="brand"><span class="brand-mark"></span>Prairie Rest CPAP</div>
    <h1 class="headline"><span class="hl-green"><span class="hl-big">80%</span> OF<br>SLEEP APNEA</span><br>CASES GO<br>UNDIAGNOSED</h1>
    <div class="rule"></div>
    <p class="intro">You wake up exhausted. You fall asleep at your desk. Your partner says you stop breathing at night. You know something's wrong.</p>
    <div class="result-box"><span>Sleep Apnea</span> Test<br>Results in less than<br>72 hours</div>
    <div class="photo-round" role="img" aria-label="Tired woman holding her head while lying in bed" style="left:336px;top:222px;width:228px;height:228px"></div>
    <div class="photo" role="img" aria-label="Hand wearing a finger sensor connected to a wrist sleep test device" style="left:311px;top:556px;width:249px;height:182px;background:linear-gradient(135deg,#dfe6f1,#aebfd8);border-radius:90px 0 0 0"></div>
    <div class="dots"></div>
    <div class="web">www.prairierestcpap.com</div>
  </article>
</section>

<!-- INNER SPREAD -->
<section class="spread spread--inner">

  <article class="page checklist-page">
    <svg class="page-bg" viewBox="0 0 560 792" aria-hidden="true">
      <path d="M0 140 C90 180 110 300 0 400Z" fill="#4cb648"/>
      <path d="M0 700 C200 684 380 698 560 666 L560 792 L0 792Z" fill="#17428a"/>
      <path d="M0 684 C200 666 380 682 560 648 L560 668 C380 700 200 686 0 704Z" fill="#4cb648"/>
    </svg>
    <p class="intro">Most people wait years before getting tested because sleep labs are expensive, inconvenient, and scheduled months out. Meanwhile you're crashing your car, destroying your health, and feeling like garbage every single day.</p>
    <div class="pill pill--green check-pill">SELF ASSESSMENT CHECKLIST</div>
    <div class="photo-round" role="img" aria-label="Woman in pajamas sitting on a bed holding her head" style="left:8px;top:166px;width:188px;height:188px"></div>
    <p class="ask">DO YOU:</p>
    <ul class="steps quiz">
      <li>Snore loudly?</li>
      <li>Wake up gasping or choking?</li>
      <li>Fall asleep during the day even when<br>you slept 8 hours?</li>
      <li>Wake up with headaches?</li>
      <li>Feel tired no matter how much you sleep?</li>
    </ul>
    <p class="verdict">If you checked 2 boxes, you probably have sleep apnea. Stop guessing. Get tested.</p>
    <div class="divider"></div>
    <div class="pill pill--green problem-pill">THE PROBLEM</div>
    <p class="subtitle">Sleep Care Wasn't Built With People In Mind.</p>
    <p class="problem-text">Most people wait months, spend a fortune and end up feeling more like a chart than a human. It doesn't have to be this way.</p>
    <p class="list-head">TRADITIONAL SLEEP LAB WORKS:</p>
    <ul class="steps lab-list">
      <li>Waiting 2–3 months just to be seen, all while you're tired, foggy,<br>and trying to keep life together</li>
      <li>Sleeping in a medical facility with 20 plus wires taped everywhere</li>
      <li>Surprise bills ranging from $1,000–$7,000</li>
      <li>Delays of weeks or months for results that should be quick</li>
      <li>Getting pushed into buying equipment at inflated prices because<br>there are no alternatives</li>
    </ul>
    <div class="dots dots--side"></div>
    <div class="dots dots--foot"></div>
    <div class="web">www.prairierestcpap.com</div>
  </article>

  <article class="page compare-page">
    <svg class="page-bg" viewBox="0 0 560 792" aria-hidden="true">
      <defs>
        <linearGradient id="topBlue" x1="0" y1="0" x2="1" y2="0">
          <stop offset="0" stop-color="#1f56a6"/>
          <stop offset="1" stop-color="#2b68b9"/>
        </linearGradient>
      </defs>
      <path d="M0 0 H560 V110 C460 112 330 140 285 196 C240 140 100 112 0 110Z" fill="url(#topBlue)"/>
      <path d="M0 106 C100 108 240 136 285 192 C330 136 460 108 560 106" fill="none" stroke="#4cb648" stroke-width="12"/>
      <path d="M0 700 C200 684 380 698 560 666 L560 792 L0 792Z" fill="#17428a"/>
      <path d="M0 684 C200 666 380 682 560 648 L560 668 C380 700 200 686 0 704Z" fill="#4cb648"/>
    </svg>
    <div class="photo-round" role="img" aria-label="Woman lying awake in bed at home" style="left:94px;top:33px;width:146px;height:146px"></div>
    <div class="photo-round" role="img" aria-label="Patient wired up for an overnight sleep lab test" style="left:331px;top:33px;width:146px;height:146px"></div>

    <div class="pill pill--green col-pill col-pill--home">Home Sleep Study</div>
    <div class="pill pill--navy col-pill col-pill--lab">In-Lab Testing</div>
    <div class="col-rule"></div>

    <ul class="features features--home">
      <li><svg viewBox="0 0 16 16" aria-hidden="true"><circle cx="8" cy="8" r="7" fill="none" stroke="#4cb648" stroke-width="1.4"/><path d="M4.6 8.2l2.2 2.2 4.6-4.8" fill="none" stroke="#4cb648" stroke-width="1.6"/></svg><h3>Comfortable</h3>A minimal device with 2 wires<br>and 3 sensors</li>
      <li><svg viewBox="0 0 16 16" aria-hidden="true"><circle cx="8" cy="8" r="7" fill="none" stroke="#4cb648" stroke-width="1.4"/><path d="M4.6 8.2l2.2 2.2 4.6-4.8" fill="none" stroke="#4cb648" stroke-width="1.6"/></svg><h3>Convenient</h3>Delivered to your door – sleep in<br>your own bed at home</li>
      <li><svg viewBox="0 0 16 16" aria-hidden="true"><circle cx="8" cy="8" r="7" fill="none" stroke="#4cb648" stroke-width="1.4"/><path d="M4.6 8.2l2.2 2.2 4.6-4.8" fill="none" stroke="#4cb648" stroke-width="1.6"/></svg><h3>Accessible</h3>Scheduling and device delivery in<br>2 - 4 business days</li>
      <li><svg viewBox="0 0 16 16" aria-hidden="true"><circle cx="8" cy="8" r="7" fill="none" stroke="#4cb648" stroke-width="1.4"/><path d="M4.6 8.2l2.2 2.2 4.6-4.8" fill="none" stroke="#4cb648" stroke-width="1.6"/></svg><h3>Affordable</h3>Pay a one-time flat fee of $189</li>
    </ul>
    <ul class="features features--lab">
      <li><svg viewBox="0 0 16 16" aria-hidden="true"><circle cx="8" cy="8" r="7" fill="none" stroke="#1f56a6" stroke-width="1.4"/><path d="M5.3 5.3l5.4 5.4M10.7 5.3l-5.4 5.4" stroke="#1f56a6" stroke-width="1.5"/></svg><h3>Invasive</h3>20–30 wires attached all over<br>your body</li>
      <li><svg viewBox="0 0 16 16" aria-hidden="true"><circle cx="8" cy="8" r="7" fill="none" stroke="#1f56a6" stroke-width="1.4"/><path d="M5.3 5.3l5.4 5.4M10.7 5.3l-5.4 5.4" stroke="#1f56a6" stroke-width="1.5"/></svg><h3>Disruptive</h3>Must sleep in a lab overnight and<br>requires travel</li>
      <li><svg viewBox="0 0 16 16" aria-hidden="true"><circle cx="8" cy="8" r="7" fill="none" stroke="#1f56a6" stroke-width="1.4"/><path d="M5.3 5.3l5.4 5.4M10.7 5.3l-5.4 5.4" stroke="#1f56a6" stroke-width="1.5"/></svg><h3>Hard to schedule</h3>Scheduling can take anywhere<br>from 3 weeks to 6 months</li>
      <li><svg viewBox="0 0 16 16" aria-hidden="true"><circle cx="8" cy="8" r="7" fill="none" stroke="#1f56a6" stroke-width="1.4"/><path d="M5.3 5.3l5.4 5.4M10.7 5.3l-5.4 5.4" stroke="#1f56a6" stroke-width="1.5"/></svg><h3>Expensive</h3>Fees can range from<br>$500 - $10,000</li>
    </ul>

    <div class="divider"></div>
    <h2 class="results"><span>SLEEP APNEA</span> TEST RESULTS<br>IN LESS THAN 72 HOURS</h2>
    <p class="results-text">Skip the labs, skip the stress, just a simple test at home. $189 with results from board certified sleep physicians.</p>
    <div class="pill pill--green order-btn">ORDER YOUR TEST KIT</div>
    <div class="photo" role="img" aria-label="Surprised woman in a blue shirt hugging a pillow and holding a test kit" style="left:331px;top:506px;width:182px;height:196px;background:linear-gradient(170deg,#eef1f6,#c9d4e6)"></div>
    <div class="dots dots--foot"></div>
    <div class="web">www.prairierestcpap.com</div>
  </article>
</section>

</body>
</html>
```